Create a dynamisch, inspiring PowerPoint Design master for our company Bridge & Grow

Core business: Coaching, Consulting and Executive search

The PPT master should be easy to use and include professional formatting (using the fonts of our website). In general, the slide master should have the look and feel of our website (in terms of fonts, colors, logos) We also would like to place big photographs on some slides, having text and graph slides as well as photo slides with just 1 key message or a citation.

The PowerPoint design should fit our corporate Identity www.bridge-grow.de
I have enclosed the PPT we use now.

Logos und colors are attached, also the master PPD we now use. We need the new master to be more modern, dynamisch und nicht so dreary, grey, but far more attractive and inspiring. If necessary we ca add a new color to make it more attractive. Please advise.

Additional information:
- wide screen format - 16:9
- creation of chart templates, using chart tools, and different chart types etc.
- creation of different slide layouts to place content, pictures (in different sizes), optionally Media
- as well as standard elements, such as text boxes, lines, default shapes, etc.

We have received your contact info and recommondations from Renate Vollmer-Stieg. We liked the master you designed very much and would like that kind of style. I can send you her presentation as a reminder if needed?

```html
<!DOCTYPE html>
<html lang="de">
<head>
<meta charset="utf-8">
<title>Bridge &amp; Grow – Presentation Master</title>
<link href="https://fonts.googleapis.com/css2?family=Righteous&family=Questrial&display=swap" rel="stylesheet">
<style>
:root{
  --teal:#1f8b85;
  --teal-dark:#13706b;
  --teal-deep:#0e5c58;
  --teal-soft:#5fb2ad;
  --panel:#eef6f7;
  --page:#e4e5e6;
  --ink:#3c3c3c;
  --grey:#7c7c7c;
  --grey-light:#c9cccd;
  --white:#ffffff;
}
*{box-sizing:border-box;margin:0;padding:0}
html,body{width:1200px;height:4208px;overflow:hidden}
body{background:var(--page);font-family:"Questrial",sans-serif;color:var(--ink);position:relative}
.head-font{font-family:"Righteous",sans-serif}

/* hero band */
.hero{position:absolute;left:0;top:0;width:1200px;height:720px}
.hero-band{fill:var(--teal)}
.hero-edge{fill:var(--white)}
.hero-brand{position:absolute;right:56px;top:48px;text-align:right;color:var(--white)}
.hero-brand .name{font-size:30px;letter-spacing:.5px;display:flex;align-items:center;gap:12px;justify-content:flex-end}
.hero-brand .name i{width:22px;height:22px;border-radius:50%;border:3px solid var(--white);display:block}
.hero-brand .tag{font-size:9px;letter-spacing:1.6px;margin-top:4px}

/* slide frame */
.slide{position:absolute;width:532px;height:297px;overflow:hidden;background:var(--white);box-shadow:0 2px 6px rgba(0,0,0,.18)}
.col-l{left:46px}.col-r{left:622px}
.r1{top:802px}.r2{top:1141px}.r3{top:1481px}.r4{top:1819px}.r5{top:2159px}
.r6{top:2497px}.r7{top:2837px}.r8{top:3175px}.r9{top:3514px}.r10{top:3854px}
.abs{position:absolute}

.logo{position:absolute;display:flex;align-items:center;gap:5px;font-size:10px;color:var(--teal);white-space:nowrap}
.logo i{width:9px;height:9px;border-radius:50%;background:var(--teal);display:block}
.logo.light{color:var(--white)}.logo.light i{background:var(--white)}
.logo-tr{right:22px;top:20px}
.logo.big{font-size:13px}.logo.big i{width:11px;height:11px}

.foot{position:absolute;left:0;right:0;bottom:10px;height:9px;background:var(--teal);color:var(--white);font-size:5.5px;line-height:9px;padding:0 26px;display:flex;justify-content:space-between}

.h-slide{position:absolute;left:26px;top:24px;font-family:"Righteous",sans-serif;color:var(--teal);font-size:15px}
.sub-h{font-family:"Righteous",sans-serif;color:var(--teal);font-size:12px;margin-bottom:4px}
.txt{font-size:10.5px;line-height:1.25;color:var(--ink)}
.txt ul{list-style:none}
.txt li{position:relative;padding-left:10px;margin-bottom:3px}
.txt li::before{content:"•";position:absolute;left:0}
.txt li.sub{padding-left:22px;font-size:9.5px}
.txt li.sub::before{content:"–";left:10px}

/* title slides */
.title-main{position:absolute;left:33px;top:44px;font-family:"Righteous",sans-serif;font-size:23px;line-height:1.33;color:var(--teal)}
.title-sub{position:absolute;left:33px;top:126px;font-size:12.5px;color:var(--grey)}
.title-rule{position:absolute;left:33px;top:170px;width:22px;height:1px;background:var(--grey)}
.title-date{position:absolute;left:33px;top:180px;font-size:9.5px;color:var(--grey)}
.photo{position:absolute}

/* toc */
.toc-item{position:absolute;left:218px;display:flex;align-items:center;gap:12px;font-size:12px;color:var(--ink)}
.toc-num{width:24px;height:24px;background:var(--teal);color:var(--white);font-family:"Righteous",sans-serif;font-size:11px;display:flex;align-items:center;justify-content:center}

.bar-row{position:absolute;left:26px;width:482px;height:24px;background:var(--teal);color:var(--white);font-size:7.5px;display:flex;align-items:center;gap:10px}
.bar-row .ico{width:24px;height:24px;background:var(--teal-dark);display:flex;align-items:center;justify-content:center}
.bar-row::after{content:"";position:absolute;right:-6px;top:0;width:4px;height:24px;background:var(--teal-dark)}

.panel-r{position:absolute;right:0;top:0;width:197px;height:277px;background:var(--panel)}

/* table */
.tbl{position:absolute;left:26px;top:50px;width:482px;border-collapse:collapse;font-size:5.8px;color:var(--ink)}
.tbl th{background:var(--teal);color:var(--white);font-weight:normal;font-family:"Righteous",sans-serif;font-size:7px;padding:3px}
.tbl tr.cap th{background:var(--teal-deep);font-size:7.5px}
.tbl td{vertical-align:top;padding:4px 6px;border-bottom:1px solid var(--grey-light);line-height:1.3}

/* team */
.member{position:absolute;width:76px;text-align:center;font-size:4.8px;line-height:1.3;color:var(--grey)}
.member .pic{width:76px;height:44px;background:linear-gradient(180deg,#d8d8d8,#9a9a9a)}
.member .nm{background:var(--teal);color:var(--white);font-family:"Righteous",sans-serif;font-size:5.5px;padding:1px 0;margin-bottom:2px;white-space:nowrap}

.num-box{width:22px;height:22px;background:var(--teal);color:var(--white);font-family:"Righteous",sans-serif;font-size:10px;display:flex;align-items:center;justify-content:center;flex:none}
.contact{position:absolute;display:flex;align-items:center;gap:10px;font-size:7px}
</style>
</head>
<body>

<!-- hero band -->
<div class="hero">
  <svg width="1200" height="720" viewBox="0 0 1200 720">
    <path class="hero-band" d="M0 0H1200V700C880 590 520 300 0 70Z"/>
    <path class="hero-edge" d="M0 110C500 330 860 610 1200 720V700C880 590 520 300 0 70Z"/>
  </svg>
  <div class="hero-brand">
    <div class="name"><i></i>bridge &amp; grow</div>
    <div class="tag">COACHING, CONSULTING UND EXECUTIVE SEARCH</div>
  </div>
</div>

<!-- 1 title light -->
<section class="slide col-l r1">
  <div class="photo" role="img" aria-label="Faint photo of a city building facade" style="inset:0;background:linear-gradient(90deg,#ffffff 30%,#ececec 100%)"></div>
  <div class="abs" style="left:282px;top:40px;width:230px;height:230px;border-radius:50%;background:var(--teal)"></div>
  <div class="title-main">Presentation<br>Title Here</div>
  <div class="title-sub">Sub Presentation Title</div>
  <div class="title-rule"></div>
  <div class="title-date">December, 2020</div>
  <div class="logo" style="left:33px;top:262px"><i></i>bridge &amp; grow</div>
</section>

<!-- 2 title light b -->
<section class="slide col-r r1">
  <div class="photo" role="img" aria-label="Faint photo of a city building facade" style="inset:0;background:linear-gradient(90deg,#ffffff 30%,#e9e9e9 100%)"></div>
  <div class="abs" style="left:300px;top:32px;width:250px;height:250px;border-radius:50%;background:var(--teal)"></div>
  <div class="title-main">Presentation<br>Title Here</div>
  <div class="title-sub">Sub Presentation Title</div>
  <div class="title-rule"></div>
  <div class="title-date">December, 2020</div>
  <div class="logo" style="left:33px;top:262px"><i></i>bridge &amp; grow</div>
</section>

<!-- 3 title teal -->
<section class="slide col-l r2" style="background:var(--teal)">
  <div class="photo" role="img" aria-label="Faint photo of a building facade in teal tones" style="inset:0;background:linear-gradient(90deg,var(--teal) 45%,#3a9a94 100%)"></div>
  <div class="abs" style="left:290px;top:36px;width:250px;height:250px;border-radius:50%;background:var(--white)"></div>
  <div class="title-main" style="color:var(--white)">Presentation<br>Title Here</div>
  <div class="title-sub" style="color:var(--white)">Sub Presentation Title</div>
  <div class="title-rule" style="background:var(--white)"></div>
  <div class="title-date" style="color:var(--white)">December, 2020</div>
  <div class="logo light" style="left:33px;top:262px"><i></i>bridge &amp; grow</div>
</section>

<!-- 4 title photo -->
<section class="slide col-r r2">
  <div class="photo" role="img" aria-label="Team photo of several consultants standing in an office" style="inset:0;background:linear-gradient(90deg,var(--teal-dark) 0%,rgba(31,139,133,.85) 35%,#8f9b9a 100%)"></div>
  <div class="abs head-font" style="left:33px;top:44px;font-size:22px;color:var(--white)">Presentation Title Here</div>
  <div class="abs" style="left:33px;top:75px;font-size:12px;color:var(--white)">Sub Presentation Title</div>
  <div class="abs" style="left:33px;top:138px;font-size:9.5px;color:var(--white)">December, 2020</div>
  <svg class="abs" style="left:0;top:200px" width="532" height="97" viewBox="0 0 532 97">
    <path d="M0 40C160 90 330 0 532 14V97H0Z" style="fill:var(--teal)"/>
    <path d="M0 62C170 100 340 18 532 30V97H0Z" style="fill:var(--white)"/>
  </svg>
  <div class="logo big" style="right:22px;top:250px"><i></i>bridge &amp; grow</div>
  <div class="abs" style="right:22px;top:268px;font-size:4.5px;color:var(--grey);letter-spacing:.6px">COACHING, CONSULTING UND EXECUTIVE SEARCH</div>
</section>

<!-- 5 toc -->
<section class="slide col-l r3">
  <div class="photo" role="img" aria-label="Office meeting room photo with teal overlay" style="left:0;top:0;width:187px;height:297px;background:linear-gradient(160deg,#4aa7a1,var(--teal-dark))"></div>
  <div class="abs head-font" style="left:0;width:187px;top:130px;text-align:center;color:var(--white);font-size:15px;line-height:1.2">Table<br>of Content</div>
  <div class="abs" style="left:187px;top:0;width:345px;height:297px;background:var(--panel)"></div>
  <div class="logo logo-tr"><i></i>bridge &amp; grow</div>
  <div class="toc-item" style="top:66px"><span class="toc-num">01</span>About Us</div>
  <div class="toc-item" style="top:107px"><span class="toc-num">02</span>Our Profile</div>
  <div class="toc-item" style="top:148px"><span class="toc-num">03</span>Our Company</div>
  <div class="toc-item" style="top:189px"><span class="toc-num">05</span>Team</div>
  <div class="toc-item" style="top:230px"><span class="toc-num">06</span>Our Activity</div>
  <div class="abs" style="right:10px;bottom:6px;font-size:5.5px;color:var(--grey)">5</div>
</section>

<!-- 6 bars -->
<section class="slide col-r r3">
  <div class="h-slide">Presentation Title Here</div>
  <div class="logo logo-tr"><i></i>bridge &amp; grow</div>
  <div class="abs" style="left:26px;top:70px;font-size:9.5px">Sint brute at usu. Duo iisque appareat adversarium at.</div>
  <div class="bar-row" style="top:94px"><span class="ico"><svg width="14" height="14" viewBox="0 0 14 14" fill="none" stroke="#fff"><circle cx="7" cy="4" r="2.5"/><path d="M2 13c0-3 2.5-5 5-5s5 2 5 5"/></svg></span>Lorem ipsum dolor sit amet, te ullum corpora delicata duo. Rebum insolens pri eu. No alia tota modus qui.</div>
  <div class="bar-row" style="top:132px"><span class="ico"><svg width="14" height="14" viewBox="0 0 14 14" fill="none" stroke="#fff"><circle cx="7" cy="7" r="5.5"/><path d="M1.5 7h11M7 1.5v11"/></svg></span>Lorem ipsum dolor sit amet, te ullum corpora delicata duo. Rebum insolens pri eu. No alia tota modus qui.</div>
  <div class="bar-row" style="top:170px"><span class="ico"><svg width="14" height="14" viewBox="0 0 14 14" fill="none" stroke="#fff"><circle cx="7" cy="4" r="2.5"/><path d="M2 13c0-3 2.5-5 5-5s5 2 5 5"/></svg></span>Lorem ipsum dolor sit amet, te ullum corpora delicata duo. Rebum insolens pri eu. No alia tota modus qui.</div>
  <div class="bar-row" style="top:208px"><span class="ico"><svg width="14" height="14" viewBox="0 0 14 14" fill="none" stroke="#fff"><circle cx="7" cy="7" r="5.5"/><path d="M1.5 7h11M7 1.5v11"/></svg></span>Lorem ipsum dolor sit amet, te ullum corpora delicata duo. Rebum insolens pri eu. No alia tota modus qui.</div>
  <div class="foot"><span>www.bridge-grow.de</span><span>6</span></div>
</section>

<!-- 7 two column -->
<section class="slide col-l r4">
  <div class="h-slide">Two Column</div>
  <div class="logo logo-tr"><i></i>bridge &amp; grow</div>
  <div class="abs txt" style="left:26px;top:60px;width:230px">
    <div class="sub-h">Lorem Ipsum</div>
    <ul>
      <li>Lorem ipsum dolor sit amet, te ullum corpora delicata duo. Rebum insolens pri eu. No alia tota modus qui.</li>
      <li class="sub">Sint brute at usu. Duo iisque appareat adversarium at.</li>
      <li>Lorem ipsum dolor sit amet, te ullum corpora delicata duo. Rebum insolens pri eu. No alia tota modus qui.</li>
      <li class="sub">Sint brute at usu. Duo iisque appareat adversarium at.</li>
    </ul>
  </div>
  <div class="abs txt" style="left:274px;top:60px;width:230px">
    <div class="sub-h">Lorem Ipsum</div>
    <ul>
      <li>Lorem ipsum dolor sit amet, te ullum corpora delicata duo. Rebum insolens pri eu. No alia tota modus qui.</li>
      <li class="sub">Sint brute at usu. Duo iisque appareat adversarium at.</li>
      <li>Lorem ipsum dolor sit amet, te ullum corpora delicata duo. Rebum insolens pri eu. No alia tota modus qui.</li>
      <li class="sub">Sint brute at usu. Duo iisque appareat adversarium at.</li>
    </ul>
  </div>
  <div class="foot"><span>www.bridge-grow.de</span><span>7</span></div>
</section>

<!-- 8 left column -->
<section class="slide col-r r4">
  <div class="h-slide">Left Column</div>
  <div class="abs txt" style="left:26px;top:60px;width:240px">
    <div class="sub-h">Lorem Ipsum</div>
    <ul>
      <li>Lorem ipsum dolor sit amet, te ullum corpora delicata duo. Rebum insolens pri eu. No alia tota modus qui.</li>
      <li class="sub">Sint brute at usu. Duo iisque appareat adversarium at.</li>
      <li>Lorem ipsum dolor sit amet, te ullum corpora delicata duo. Rebum insolens pri eu. No alia tota modus qui.</li>
      <li class="sub">Sint brute at usu. Duo iisque appareat adversarium at.</li>
    </ul>
  </div>
  <div class="photo" role="img" aria-label="Photo of a consultant presenting at a flipchart in an office" style="left:290px;top:0;width:242px;height:277px;background:linear-gradient(180deg,#f0f0f0,#b9b9b9)"></div>
  <div class="abs" style="left:290px;top:226px;width:160px;height:38px;background:var(--teal);color:var(--white);padding:6px 8px">
    <div class="head-font" style="font-size:10px">John Doe</div>
    <div style="font-size:6px">Director</div>
  </div>
  <div class="foot"><span>www.bridge-grow.de</span><span>8</span></div>
</section>

<!-- 9 content + right column -->
<section class="slide col-l r5">
  <div class="h-slide">Content and Right Column</div>
  <div class="logo logo-tr"><i></i>bridge &amp; grow</div>
  <div class="photo" role="img" aria-label="Laptop showing the company website" style="left:20px;top:82px;width:230px;height:140px;background:linear-gradient(180deg,#4a4a4a,#1c1c1c);border-radius:4px"></div>
  <div class="abs txt" style="left:283px;top:90px;width:225px">
    Lorem ipsum dolor sit amet, te ullum corpora delicata duo. Rebum insolens pri eu. Lorem ipsum dolor sit amet, te ullum corpora delicata duo. Rebum insolens pri eu. No alia tota modus qui.
    <ul style="margin-top:3px"><li>Sint brute at usu. Duo iisque appareat adversarium at.</li></ul>
  </div>
  <div class="foot"><span>www.bridge-grow.de</span><span>9</span></div>
</section>

<!-- 10 divider -->
<section class="slide col-r r5" style="background:var(--teal)">
  <div class="photo" role="img" aria-label="Faint photo of people in a meeting, teal tinted" style="inset:0;background:linear-gradient(90deg,var(--teal) 40%,#4fa49f 100%)"></div>
  <div class="abs" style="left:320px;top:90px;width:300px;height:300px;border-radius:50%;background:var(--white)"></div>
  <svg class="abs" style="left:33px;top:134px" width="34" height="34" viewBox="0 0 34 34" fill="none" stroke="#fff" stroke-width="1.4"><circle cx="10" cy="8" r="4"/><circle cx="24" cy="8" r="4"/><path d="M3 20c0-4 3-6 7-6s7 2 7 6M17 20c0-4 3-6 7-6s7 2 7 6"/><circle cx="10" cy="24" r="3"/><circle cx="24" cy="24" r="3"/></svg>
  <div class="abs head-font" style="left:33px;top:190px;font-size:17px;color:var(--white)">Divider Slide</div>
  <div class="abs" style="left:33px;top:214px;font-size:11px;color:var(--white)">Sub Divider Slide</div>
  <div class="logo big" style="right:24px;top:260px"><i></i>bridge &amp; grow</div>
</section>

<!-- 11 bar chart -->
<section class="slide col-l r6">
  <div class="panel-r"></div>
  <div class="h-slide">Bar Chart Sample</div>
  <div class="logo logo-tr"><i></i>bridge &amp; grow</div>
  <svg class="abs" style="left:16px;top:78px" width="250" height="160" viewBox="0 0 250 160" font-size="6" fill="#9a9a9a">
    <g text-anchor="end"><text x="24" y="14">6</text><text x="24" y="35">5</text><text x="24" y="56">4</text><text x="24" y="77">3</text><text x="24" y="98">2</text><text x="24" y="119">1</text><text x="24" y="140">0</text></g>
    <g>
      <rect x="34" y="47" width="10" height="91" style="fill:var(--teal)"/><rect x="45" y="88" width="10" height="50" style="fill:var(--grey)"/><rect x="56" y="97" width="10" height="41" style="fill:var(--teal-dark)"/>
      <rect x="84" y="88" width="10" height="50" style="fill:var(--teal)"/><rect x="95" y="45" width="10" height="93" style="fill:var(--grey)"/><rect x="106" y="97" width="10" height="41" style="fill:var(--teal-dark)"/>
      <rect x="134" y="64" width="10" height="74" style="fill:var(--teal)"/><rect x="145" y="100" width="10" height="38" style="fill:var(--grey)"/><rect x="156" y="76" width="10" height="62" style="fill:var(--teal-dark)"/>
      <rect x="184" y="47" width="10" height="91" style="fill:var(--teal)"/><rect x="195" y="80" width="10" height="58" style="fill:var(--grey)"/><rect x="206" y="35" width="10" height="103" style="fill:var(--teal-dark)"/>
    </g>
    <g text-anchor="middle"><text x="50" y="150">Category 1</text><text x="100" y="150">Category 2</text><text x="150" y="150">Category 3</text><text x="200" y="150">Category 4</text></g>
    <g><rect x="70" y="155" width="5" height="3" style="fill:var(--teal)"/><text x="77" y="158">Series 1</text><rect x="105" y="155" width="5" height="3" style="fill:var(--grey)"/><text x="112" y="158">Series 2</text><rect x="140" y="155" width="5" height="3" style="fill:var(--teal-dark)"/><text x="147" y="158">Series 3</text></g>
  </svg>
  <div class="abs txt" style="left:350px;top:62px;width:170px">
    <div class="sub-h">Lorem Ipsum</div>
    <ul>
      <li>Lorem ipsum dolor sit amet, te ullum corpora delicata duo. Rebum insolens pri eu. No alia tota modus qui.</li>
      <li class="sub">Sint brute at usu. Duo iisque appareat adversarium at.</li>
      <li>Lorem ipsum dolor sit amet, te ullum corpora delicata duo. Rebum insolens pri eu. No alia tota modus qui.</li>
    </ul>
  </div>
  <div class="foot"><span>www.bridge-grow.de</span><span>11</span></div>
</section>

<!-- 12 line chart -->
<section class="slide col-r r6">
  <div class="panel-r"></div>
  <div class="h-slide">Line Chart Sample</div>
  <div class="logo logo-tr"><i></i>bridge &amp; grow</div>
  <svg class="abs" style="left:16px;top:68px" width="250" height="170" viewBox="0 0 250 170" font-size="6" fill="#9a9a9a">
    <g text-anchor="end"><text x="24" y="14">6</text><text x="24" y="38">5</text><text x="24" y="62">4</text><text x="24" y="86">3</text><text x="24" y="110">2</text><text x="24" y="134">1</text><text x="24" y="158">0</text></g>
    <polyline points="50,62 105,104 160,76 215,60" fill="none" style="stroke:var(--teal)" stroke-width="1.5"/>
    <polyline points="50,105 105,62 160,110 215,40" fill="none" style="stroke:var(--teal-deep)" stroke-width="1.5"/>
    <polyline points="50,110 105,110 160,96 215,86" fill="none" style="stroke:var(--grey)" stroke-width="1.5"/>
    <g text-anchor="middle"><text x="50" y="166">Category 1</text><text x="105" y="166">Category 2</text><text x="160" y="166">Category 3</text><text x="215" y="166">Category 4</text></g>
  </svg>
  <div class="abs" style="left:70px;top:246px;font-size:6px;color:#9a9a9a">— Series 1 &nbsp; — Series 2 &nbsp; — Series 3</div>
  <div class="abs txt" style="left:350px;top:62px;width:170px">
    <div class="sub-h">Lorem Ipsum</div>
    <ul>
      <li>Lorem ipsum dolor sit amet, te ullum corpora delicata duo. Rebum insolens pri eu. No alia tota modus qui.</li>
      <li class="sub">Sint brute at usu. Duo iisque appareat adversarium at.</li>
      <li>Lorem ipsum dolor sit amet, te ullum corpora delicata duo. Rebum insolens pri eu. No alia tota modus qui.</li>
    </ul>
  </div>
  <div class="foot"><span>www.bridge-grow.de</span><span>12</span></div>
</section>

<!-- 13 pie chart -->
<section class="slide col-l r7">
  <div class="panel-r"></div>
  <div class="h-slide">Pie Chart Sample</div>
  <div class="logo logo-tr"><i></i>bridge &amp; grow</div>
  <svg class="abs" style="left:60px;top:70px" width="180" height="180" viewBox="-90 -90 180 180" font-family="Questrial, sans-serif">
    <path d="M0 0L0 -80A80 80 0 0 1 77.4 20.2Z" style="fill:var(--teal)"/>
    <path d="M0 0L77.4 20.2A80 80 0 0 1 20.2 77.4Z" style="fill:var(--teal-dark)"/>
    <path d="M0 0L20.2 77.4A80 80 0 0 1 -75.4 26.7Z" style="fill:var(--grey)"/>
    <path d="M0 0L-75.4 26.7A80 80 0 0 1 0 -80Z" style="fill:var(--teal-deep)"/>
    <g fill="#fff" font-size="13" text-anchor="middle"><text x="35" y="-20">4,3</text><text x="38" y="40">2,5</text><text x="-25" y="50">3,5</text><text x="-40" y="-10">4,5</text></g>
  </svg>
  <div class="abs" style="left:50px;top:260px;font-size:6px;color:#9a9a9a">■ Category 1 &nbsp; ■ Category 2 &nbsp; ■ Category 3 &nbsp; ■ Category 4</div>
  <div class="abs txt" style="left:350px;top:62px;width:170px">
    <div class="sub-h">Lorem Ipsum</div>
    <ul>
      <li>Lorem ipsum dolor sit amet, te ullum corpora delicata duo. Rebum insolens pri eu. No alia tota modus qui.</li>
      <li class="sub">Sint brute at usu. Duo iisque appareat adversarium at.</li>
      <li>Lorem ipsum dolor sit amet, te ullum corpora delicata duo. Rebum insolens pri eu. No alia tota modus qui.</li>
    </ul>
  </div>
  <div class="foot"><span>www.bridge-grow.de</span><span>13</span></div>
</section>

<!-- 14 table -->
<section class="slide col-r r7">
  <div class="h-slide">Table Sample</div>
  <div class="logo logo-tr"><i></i>bridge &amp; grow</div>
  <table class="tbl">
    <tr class="cap"><th colspan="4">LOREM IPSUM</th></tr>
    <tr><th>Lorem Ipsum</th><th>Lorem Ipsum 1</th><th>Lorem Ipsum 2</th><th>Lorem Ipsum 3</th></tr>
    <tr><td>• Lorem ipsum dolor sit amet, consectetur adipiscing elit.<br>• Quisque nec enim luctus, finibus leo vulputate.</td><td>• Lorem ipsum dolor sit amet, consectetur adipiscing elit.</td><td>• Lorem ipsum dolor sit amet, consectetur adipiscing elit.</td><td>• Lorem ipsum dolor sit amet, consectetur adipiscing elit.<br>• Quisque nec enim luctus, finibus leo vulputate.</td></tr>
    <tr><td>• Lorem ipsum dolor sit amet, consectetur adipiscing elit.</td><td>• Lorem ipsum dolor sit amet, consectetur adipiscing elit.</td><td>• Lorem ipsum dolor sit amet, consectetur adipiscing elit, finibus leo vulputate.</td><td>• Lorem ipsum dolor sit amet, consectetur adipiscing elit, finibus leo vulputate.</td></tr>
    <tr><td>• Lorem ipsum dolor sit amet, consectetur adipiscing elit.</td><td>• Lorem ipsum dolor sit amet, consectetur adipiscing elit.</td><td>• Lorem ipsum dolor sit amet, consectetur adipiscing elit.</td><td>• Lorem ipsum dolor sit amet, consectetur adipiscing elit.</td></tr>
    <tr><td>• Lorem ipsum dolor sit amet, consectetur adipiscing elit.</td><td>• Lorem ipsum dolor sit amet, consectetur adipiscing elit.</td><td>• Lorem ipsum dolor sit amet, consectetur adipiscing elit.</td><td>• Lorem ipsum dolor sit amet, consectetur adipiscing elit.</td></tr>
  </table>
  <div class="foot"><span>www.bridge-grow.de</span><span>14</span></div>
</section>

<!-- 15 team -->
<section class="slide col-l r8">
  <div class="h-slide">Unser Team</div>
  <div class="logo logo-tr"><i></i>bridge &amp; grow</div>
  <div class="member" style="left:26px;top:64px"><div class="pic" role="img" aria-label="Portrait photo of a team member"></div><div class="nm">Anna Keller</div>Individual und Business Coaching, Intercultural Competence</div>
  <div class="member" style="left:123px;top:64px"><div class="pic" role="img" aria-label="Portrait photo of a team member"></div><div class="nm">Paul Brandt</div>Executive Search, Management Diagnostik, Karrierecoaching</div>
  <div class="member" style="left:220px;top:64px"><div class="pic" role="img" aria-label="Portrait photo of a team member"></div><div class="nm">Sara Lindner</div>Individual und Business Coaching, New Leadership</div>
  <div class="member" style="left:317px;top:64px"><div class="pic" role="img" aria-label="Portrait photo of a team member"></div><div class="nm">Jonas Weber</div>Executive Search, Branchenübergreifende Digitalexpertise</div>
  <div class="member" style="left:414px;top:64px"><div class="pic" role="img" aria-label="Portrait photo of a team member"></div><div class="nm">Eva Hartmann</div>Mensch-Computer Interaktion, Nutzerzentriertes Design</div>
  <div class="member" style="left:26px;top:168px"><div class="pic" role="img" aria-label="Portrait photo of a team member"></div><div class="nm">Clara Moser</div>Individual und Business Coaching, Führungskräfte Entwicklung</div>
  <div class="member" style="left:123px;top:168px"><div class="pic" role="img" aria-label="Portrait photo of a team member"></div><div class="nm">Lena Fuchs</div>Projektmanagement, Marketing, Controlling</div>
  <div class="member" style="left:220px;top:168px"><div class="pic" role="img" aria-label="Portrait photo of a team member"></div><div class="nm">Tobias Kern</div>Business Development, Innovationsmanagement</div>
  <div class="member" style="left:317px;top:168px"><div class="pic" role="img" aria-label="Portrait photo of a team member"></div><div class="nm">Marie Sommer</div>Individual und Business Coaching, Teamentwicklung, Workshops</div>
  <div class="member" style="left:414px;top:168px"><div class="pic" role="img" aria-label="Portrait photo of a team member"></div><div class="nm">Renate Vollmer-Stieg</div>Beratung in strategischen Positionierungs- und Transformationsprozessen</div>
  <div class="foot"><span>www.bridge-grow.de</span><span>15</span></div>
</section>

<!-- 16 our business -->
<section class="slide col-r r8">
  <div class="photo" role="img" aria-label="Two photos of consultants in conversation" style="left:0;top:0;width:532px;height:128px;background:linear-gradient(90deg,#ffffff 0%,#d5d5d5 35%,#a9a9a9 55%,#e0e0e0 100%)"></div>
  <div class="h-slide">Our Business</div>
  <div class="logo logo-tr"><i></i>bridge &amp; grow</div>
  <div class="abs" style="left:30px;top:110px;width:30px;height:30px;border-radius:50%;background:var(--teal);border:2px solid #fff"></div>
  <div class="abs" style="left:275px;top:110px;width:30px;height:30px;border-radius:50%;background:var(--teal-deep);border:2px solid #fff"></div>
  <div class="abs txt" style="left:30px;top:150px;width:225px">Lorem ipsum dolor sit amet, te ullum corpora delicata duo. Rebum insolens pri eu. No alia tota modus qui.<ul style="margin-top:5px"><li>Rebum insolens pri eu. No alia tota modus qui</li></ul></div>
  <div class="abs txt" style="left:282px;top:150px;width:225px">Lorem ipsum dolor sit amet, te ullum corpora delicata duo. Rebum insolens pri eu. No alia tota modus qui.<ul style="margin-top:5px"><li>Rebum insolens pri eu. No alia tota modus qui</li></ul></div>
  <div class="foot"><span>www.bridge-grow.de</span><span>16</span></div>
</section>

<!-- 17 our report -->
<section class="slide col-l r9">
  <div class="abs" style="left:0;top:0;width:252px;height:297px;background:var(--teal)"></div>
  <div class="abs" style="left:252px;top:0;width:280px;height:297px;background:var(--panel)"></div>
  <div class="h-slide" style="color:var(--white)">Our Report</div>
  <div class="logo logo-tr"><i></i>bridge &amp; grow</div>
  <div class="abs txt" style="left:32px;top:80px;width:120px;color:var(--white)">
    <div class="sub-h" style="color:var(--white)">Lorem Ipsum</div>
    <ul><li>Lorem ipsum dolor sit amet, te ullum delicata duo. Rebum insolens pri eu. No alia tota modus.</li><li class="sub">Sint brute at usu. Duo iisque appareat adversarium at.</li></ul>
  </div>
  <div class="photo" role="img" aria-label="Tablet showing a report document" style="left:172px;top:60px;width:158px;height:205px;background:linear-gradient(180deg,#2a2a2a,#101010);border-radius:8px"></div>
  <div class="abs" style="left:330px;top:96px;display:flex;flex-direction:column;gap:20px">
    <div style="display:flex;gap:8px;align-items:center"><span class="num-box">01</span><span class="txt" style="font-size:8px">Lorem ipsum dolor<br>sit amet, te ullum delicata duo.</span></div>
    <div style="display:flex;gap:8px;align-items:center"><span class="num-box">02</span><span class="txt" style="font-size:8px">Lorem ipsum dolor<br>sit amet, te ullum delicata duo.</span></div>
    <div style="display:flex;gap:8px;align-items:center"><span class="num-box">03</span><span class="txt" style="font-size:8px">Lorem ipsum dolor<br>sit amet, te ullum delicata duo.</span></div>
  </div>
</section>

<!-- 18 divider b -->
<section class="slide col-r r9" style="background:var(--teal)">
  <div class="photo" role="img" aria-label="Faint photo of an office meeting, teal tinted" style="inset:0;background:linear-gradient(90deg,var(--teal) 30%,#2f968f 100%)"></div>
  <div class="abs" style="left:335px;top:-150px;width:300px;height:300px;border-radius:50%;background:var(--white)"></div>
  <div class="logo big" style="right:24px;top:24px"><i></i>bridge &amp; grow</div>
  <svg class="abs" style="left:33px;top:136px" width="34" height="34" viewBox="0 0 34 34" fill="none" stroke="#fff" stroke-width="1.4"><circle cx="17" cy="17" r="14"/><circle cx="17" cy="17" r="6"/><path d="M17 3v8M17 23v8M3 17h8M23 17h8"/></svg>
  <div class="abs head-font" style="left:33px;top:190px;font-size:17px;color:var(--white)">Divider Slide</div>
  <div class="abs" style="left:33px;top:214px;font-size:11px;color:var(--white)">Sub Divider Slide</div>
</section>

<!-- 19 thank you light -->
<section class="slide col-l r10">
  <div class="photo" role="img" aria-label="Faint photo of a bright office interior" style="inset:0;background:linear-gradient(90deg,#ffffff 40%,#e4e4e4 100%)"></div>
  <svg class="abs" style="left:0;top:0" width="532" height="297" viewBox="0 0 532 297">
    <path d="M180 0C330 60 300 210 532 262V297H410C300 230 330 90 180 0Z" style="fill:var(--teal)"/>
  </svg>
  <div class="abs head-font" style="left:18px;top:44px;font-size:17px;color:var(--teal-deep)">Thank You</div>
  <div class="abs" style="left:18px;top:74px;width:230px;font-size:7.5px;line-height:1.3">Lorem Ipsum is simply dummy text of the printing and typesetting industry. Lorem Ipsum has been the industry's standard dummy text ever since the 1500s, when an unknown printer took a galley of type and scrambled it to make a type specimen book.</div>
  <div class="contact" style="left:18px;top:152px"><svg width="9" height="7" viewBox="0 0 9 7"><rect width="9" height="7" style="fill:var(--teal)"/><path d="M0 0l4.5 4L9 0" stroke="#fff" fill="none"/></svg>Lorem ipsum</div>
  <div class="contact" style="left:18px;top:174px"><span style="width:9px;height:9px;background:var(--teal);display:block"></span>Lorem ipsum</div>
  <div class="contact" style="left:18px;top:196px"><svg width="8" height="10" viewBox="0 0 8 10"><path d="M4 10C1 6 0 5 0 4a4 4 0 0 1 8 0c0 1-1 2-4 6Z" style="fill:var(--teal)"/><circle cx="4" cy="4" r="1.4" fill="#fff"/></svg>Lorem ipsum</div>
  <div class="logo" style="left:18px;top:262px"><i></i>bridge &amp; grow</div>
</section>

<!-- 20 thank you teal -->
<section class="slide col-r r10" style="background:var(--teal)">
  <div class="photo" role="img" aria-label="Faint office interior photo, teal tinted" style="inset:0;background:linear-gradient(90deg,var(--teal) 45%,#3d9c96 100%)"></div>
  <svg class="abs" style="left:0;top:0" width="532" height="297" viewBox="0 0 532 297">
    <path d="M250 0C380 50 360 200 532 250V0Z" style="fill:var(--white)"/>
    <path d="M532 250C450 232 420 200 400 170C440 230 490 262 532 270Z" style="fill:var(--teal-deep)"/>
  </svg>
  <div class="abs head-font" style="left:18px;top:44px;font-size:17px;color:var(--white)">Thank You</div>
  <div class="abs" style="left:18px;top:74px;width:230px;font-size:7.5px;line-height:1.3;color:var(--white)">Lorem Ipsum is simply dummy text of the printing and typesetting industry. Lorem Ipsum has been the industry's standard dummy text ever since the 1500s, when an unknown printer took a galley of type and scrambled it to make a type specimen book.</div>
  <div class="contact" style="left:18px;top:152px;color:var(--white)"><svg width="9" height="7" viewBox="0 0 9 7"><rect width="9" height="7" fill="#fff"/><path d="M0 0l4.5 4L9 0" style="stroke:var(--teal)" fill="none"/></svg>Lorem ipsum</div>
  <div class="contact" style="left:18px;top:174px;color:var(--white)"><span style="width:9px;height:9px;background:#fff;display:block"></span>Lorem ipsum</div>
  <div class="contact" style="left:18px;top:196px;color:var(--white)"><svg width="8" height="10" viewBox="0 0 8 10"><path d="M4 10C1 6 0 5 0 4a4 4 0 0 1 8 0c0 1-1 2-4 6Z" fill="#fff"/><circle cx="4" cy="4" r="1.4" style="fill:var(--teal)"/></svg>Lorem ipsum</div>
  <div class="logo big light" style="right:24px;top:262px"><i></i>bridge &amp; grow</div>
</section>

</body>
</html>
```